Quick Straightforward Billboard Redesign

- Design billboard sized for 10 foot' x 36' foot width live area size and please include bleeds 6" around all sides
- Exact blue color match is imperative in headline, logo, phone number bubble or wherever used. C-83 / M-45 / Y-1 / K-0-
- What I hope to illustrate is that our company offers the best porch screening in the area area, in regards to quality, expertise, durability, storms proof, but we do not build screen porches.
- Current board is attached below from previous designer, and as you can see sizing was off, white space on edges make it appear to be sized incorrectly.
- I also attached my own little mock up idea well well if it helps, favorite image, logo, headline, etc and ideas perhaps on expanding or making this better?

Thanks so much!

Target Market(s)

Drivers and passengers, Southeastern NC, are of immense new construction and high end homes.

Industry/Entity Type

Construction

Colors
0054AA
0677BA
7BADD7
CADEEF
E8F1F8

Requirements
Must have
• Blue color matching
Nice to have
• Design spins or other thoughts on my little mock up

```html
<!DOCTYPE html>
<html lang="en">
<head>
<meta charset="utf-8">
<title>Tidewater Porch Screens Billboard</title>
<link href="https://fonts.googleapis.com/css2?family=Anton&family=Montserrat:wght@800&display=swap" rel="stylesheet">
<style>
  :root {
    --brand-blue: #0054AA;
    --band-blue: #0067B4;
    --accent-green: #0BAF4F;
    --panel-light: #F0F1F2;
    --page-bg: #E8F1F8;
    --white: #FFFFFF;
  }
  html, body {
    margin: 0;
    padding: 0;
    width: 1200px;
    height: 1091px;
    overflow: hidden;
    background: var(--page-bg);
  }
  .billboard {
    position: absolute;
    left: 40px;
    top: 382px;
    width: 1120px;
    height: 326px;
    overflow: hidden;
    background: var(--panel-light);
    box-shadow: 0 6px 20px rgba(0, 40, 90, 0.18);
  }
  .billboard-shapes {
    position: absolute;
    inset: 0;
  }
  .brand-name {
    position: absolute;
    left: 66px;
    top: 38px;
    margin: 0;
    font-family: "Anton", Impact, sans-serif;
    font-weight: 400;
    font-size: 40px;
    line-height: 1;
    letter-spacing: 0.5px;
    color: var(--brand-blue);
    display: flex;
    align-items: center;
    gap: 14px;
  }
  .brand-square {
    width: 30px;
    height: 30px;
    background: var(--brand-blue);
  }
  .headline {
    position: absolute;
    left: 48px;
    top: 110px;
    margin: 0;
    font-family: "Anton", Impact, sans-serif;
    font-weight: 400;
    font-size: 56px;
    line-height: 66px;
    letter-spacing: 2px;
    text-shadow: 3px 3px 0 rgba(0, 30, 70, 0.45);
  }
  .headline-line { display: block; }
  .headline-line--white { color: var(--white); }
  .headline-line--green { color: var(--accent-green); }
  .phone {
    position: absolute;
    left: 88px;
    top: 263px;
    display: flex;
    align-items: center;
    gap: 18px;
    font-family: "Montserrat", Arial, sans-serif;
    font-weight: 800;
    font-size: 46px;
    line-height: 1;
    color: var(--brand-blue);
    text-shadow: 2px 2px 0 rgba(0, 30, 70, 0.25);
  }
  .phone-icon { width: 44px; height: 44px; }
</style>
</head>
<body>
  <div class="billboard">
    <svg class="billboard-shapes" viewBox="0 0 1120 326" width="1120" height="326" aria-hidden="false">
      <defs>
        <linearGradient id="porchPhoto" x1="0" y1="0" x2="0" y2="1">
          <stop offset="0" stop-color="#E9ECEE"/>
          <stop offset="0.22" stop-color="#CFE2F2"/>
          <stop offset="0.42" stop-color="#8FB7D6"/>
          <stop offset="0.55" stop-color="#9DB377"/>
          <stop offset="0.68" stop-color="#8D7F6E"/>
          <stop offset="1" stop-color="#D8D1C4"/>
        </linearGradient>
      </defs>
      <rect class="headline-band" x="0" y="102" width="720" height="148" fill="var(--band-blue)"/>
      <path class="photo-area" role="img" aria-label="Photo of a covered screened porch with wicker lounge chairs overlooking a lake"
            d="M756,0 Q660,160 738,326 L1120,326 L1120,0 Z" fill="url(#porchPhoto)"/>
      <path class="photo-frame-curve" d="M730,0 Q632,160 684,326 L738,326 Q660,160 756,0 Z" fill="var(--band-blue)"/>
    </svg>

    <h2 class="brand-name"><span class="brand-square"></span>TIDEWATER PORCH SCREENS</h2>

    <h1 class="headline">
      <span class="headline-line headline-line--white">SCREEN YOUR PORCH.</span>
      <span class="headline-line headline-line--green">BUILT FOR THE COAST.</span>
    </h1>

    <div class="phone">
      <svg class="phone-icon" viewBox="0 0 44 44" aria-hidden="true">
        <circle cx="22" cy="22" r="22" fill="var(--accent-green)"/>
        <path d="M15.5 11.5c1-.6 2-.3 2.6.6l2.3 3.6c.5.9.3 2-.5 2.6l-1.7 1.2c1 2.6 3.2 5 5.9 6.3l1.3-1.6c.7-.8 1.8-1 2.7-.4l3.5 2.4c.9.6 1.1 1.8.5 2.7l-1.4 2c-.8 1.1-2.2 1.6-3.6 1.2-7.3-2.2-12.6-7.8-14.4-15.1-.3-1.3.2-2.7 1.3-3.5z" fill="var(--white)"/>
      </svg>
      <span class="phone-number">910.555.0148</span>
    </div>
  </div>
</body>
</html>
```